Marlow Law Stationery - Letterhead, Envelopes, Business Cards

We need high quality business stationery for our Personal Injury Law Firm located in Houston, Texas. The design should include the logo, Marlow Law Group, PLLC, 713-555-4718, 2150 Fernbrook Avenue, Suite 310, Houston, Texas 77019 www.MarlowLaw.example. The colors are blue and white. The letterhead should also include the Attorneys - Tessa Quill, Mitchell R. Marlow and Derek Hale.

```html
<!DOCTYPE html>
<html lang="en">
<head>
<meta charset="utf-8">
<title>Marlow Law Group Stationery</title>
<link href="https://fonts.googleapis.com/css2?family=Arimo:wght@400&family=Montserrat:wght@500;600;700&display=swap" rel="stylesheet">
<style>
  :root {
    --navy: #0d1b3e;
    --paper: #ffffff;
    --backdrop: #e6e6e6;
    --ink: #111111;
    --signature-tone: #eef0f4;
  }
  * { box-sizing: border-box; margin: 0; padding: 0; }
  html, body { width: 1200px; height: 1200px; overflow: hidden; }
  body { background: var(--backdrop); position: relative; font-family: "Montserrat", sans-serif; color: var(--navy); }

  .letterhead { position: absolute; left: 220px; top: 108px; width: 765px; height: 989px; background: var(--paper); }
  .letterhead-band { position: absolute; left: 0; top: 0; width: 42px; height: 100%; background: var(--navy); }

  .brand-mark { position: absolute; font-weight: 700; text-align: center; }

  .letterhead .brand-mark { left: 66px; top: 58px; width: 136px; font-size: 26px; line-height: 30px; color: var(--navy); }

  .firm-name { position: absolute; left: 218px; top: 75px; font-size: 22px; font-weight: 700; letter-spacing: 0.4px; white-space: nowrap; }
  .firm-rule { position: absolute; left: 218px; right: 0; top: 103px; height: 2px; background: var(--navy); }
  .firm-tagline { position: absolute; left: 218px; top: 108px; font-size: 18.5px; font-weight: 500; letter-spacing: 2.5px; }

  .letter-date { position: absolute; right: 54px; top: 200px; font-family: "Arimo", sans-serif; font-size: 15.5px; color: var(--ink); letter-spacing: 0.6px; }
  .letter-body { position: absolute; left: 196px; top: 227px; font-family: "Arimo", sans-serif; font-size: 15.5px; line-height: 33.2px; color: var(--ink); letter-spacing: 0.8px; white-space: nowrap; }
  .letter-signoff { position: absolute; left: 196px; top: 699px; font-family: "Arimo", sans-serif; font-size: 15.5px; color: var(--ink); letter-spacing: 0.8px; }
  .signature-area { position: absolute; left: 196px; top: 728px; width: 86px; height: 46px; background: var(--signature-tone); }

  .letter-footer { position: absolute; left: 182px; top: 869px; width: 560px; height: 94px; }
  .attorney-list { position: absolute; left: 0; top: 0; border-left: 2px solid var(--navy); padding-left: 13px; height: 94px; font-size: 12.5px; font-weight: 500; line-height: 22px; padding-top: 2px; }
  .attorney-list .heading { font-weight: 700; }
  .contact-list { position: absolute; left: 300px; top: 8px; font-size: 12.5px; font-weight: 500; }
  .contact-item { display: flex; gap: 6px; align-items: flex-start; line-height: 12.5px; }
  .contact-item svg { flex: none; margin-top: 1px; }
  .contact-item + .contact-item { margin-top: 14px; }

  .card { position: absolute; width: 315px; height: 180px; overflow: hidden; }
  .card-front { left: 825px; top: 546px; background: var(--navy); color: var(--paper); }
  .card-front .brand-mark { left: 0; right: 0; top: 50px; font-size: 22px; line-height: 26px; display: flex; justify-content: center; align-items: center; gap: 10px; }
  .card-front .brand-mark .dot { width: 30px; height: 30px; border-radius: 50%; background: var(--paper); }
  .card-front .card-name { position: absolute; left: 0; right: 0; top: 125px; text-align: center; font-size: 12px; font-weight: 700; letter-spacing: 0.4px; }
  .card-front .card-rule { position: absolute; left: 62px; right: 62px; top: 143px; height: 1px; background: var(--paper); }
  .card-front .card-tagline { position: absolute; left: 0; right: 0; top: 146px; text-align: center; font-size: 10.5px; font-weight: 500; letter-spacing: 1.4px; }

  .card-back { left: 826px; top: 759px; height: 179px; background: var(--paper); }
  .card-back-band { position: absolute; left: 0; top: 0; width: 56px; height: 100%; background: var(--navy); }
  .card-back .brand-mark { left: 24px; top: 24px; width: 64px; height: 58px; padding-top: 10px; font-size: 13px; line-height: 19px; color: var(--navy); background: var(--paper); border-radius: 4px; }
  .card-back .card-name { position: absolute; left: 96px; top: 43px; font-size: 11px; font-weight: 700; white-space: nowrap; }
  .card-back .card-rule { position: absolute; left: 96px; right: 0; top: 57px; height: 1px; background: var(--navy); }
  .card-back .card-tagline { position: absolute; left: 96px; top: 61px; font-size: 8.5px; font-weight: 500; letter-spacing: 1px; }
  .card-back .person { position: absolute; left: 97px; top: 85px; font-size: 12.5px; font-weight: 700; }
  .card-back .card-contacts { position: absolute; left: 97px; top: 110px; font-size: 8.5px; font-weight: 500; }
  .card-back .card-contacts .contact-item { gap: 4px; line-height: 10px; }
  .card-back .card-contacts .contact-item + .contact-item { margin-top: 3px; }
</style>
</head>
<body>

<section class="letterhead">
  <div class="letterhead-band"></div>
  <div class="brand-mark">Marlow<br>Law</div>
  <div class="firm-name">MARLOW LAW GROUP, PLLC</div>
  <div class="firm-rule"></div>
  <div class="firm-tagline">INJURY ATTORNEYS</div>

  <div class="letter-date">July 16, 2026</div>
  <div class="letter-body">
    Dear Tessa,<br>
    Thank you for inviting me to design your new letterhead.<br>
    This letterhead is designed to embody simplicity, professionalism,<br>
    and brand consistency. By using a clean layout with generous white<br>
    space, the design ensures readability and a modern, uncluttered<br>
    look. Your logo is placed prominently but tastefully, reinforcing<br>
    brand recognition without overpowering the content.<br>
    Professional sans serif typography complements<br>
    the contemporary style, ensuring that official<br>
    correspondence looks polished and credible.<br>
    Overall, the design balances corporate sophistication<br>
    with the energetic, spirit that defines MARLOW LAW.<br>
    I hope you like it.
  </div>
  <div class="letter-signoff">Best Regards,</div>
  <div class="signature-area" role="img" aria-label="Handwritten signature of the letter writer"></div>

  <footer class="letter-footer">
    <div class="attorney-list">
      <div class="heading">Attorneys</div>
      <div>Tessa Quill</div>
      <div>Mitchell R. Marlow</div>
      <div>Derek Hale</div>
    </div>
    <div class="contact-list">
      <div class="contact-item">
        <svg width="11" height="11" viewBox="0 0 24 24"><path fill="#0d1b3e" d="M6.6 10.8a15 15 0 0 0 6.6 6.6l2.2-2.2a1 1 0 0 1 1-.25 11 11 0 0 0 3.6.6 1 1 0 0 1 1 1V20a1 1 0 0 1-1 1A17 17 0 0 1 3 4a1 1 0 0 1 1-1h3.5a1 1 0 0 1 1 1c0 1.25.2 2.45.6 3.6a1 1 0 0 1-.25 1z"/></svg>
        <span>713-555-4718</span>
      </div>
      <div class="contact-item">
        <svg width="10" height="12" viewBox="0 0 20 24"><path fill="#0d1b3e" d="M10 0a8 8 0 0 0-8 8c0 6 8 16 8 16s8-10 8-16a8 8 0 0 0-8-8zm0 11a3 3 0 1 1 0-6 3 3 0 0 1 0 6z"/></svg>
        <span>2150 Fernbrook Avenue, Suite 310,<br>Houston, Texas 77019</span>
      </div>
      <div class="contact-item">
        <svg width="10" height="10" viewBox="0 0 20 20"><circle cx="10" cy="10" r="8.5" fill="none" stroke="#0d1b3e" stroke-width="2"/><path d="M1.5 10h17M10 1.5c-4 4.5-4 12.5 0 17M10 1.5c4 4.5 4 12.5 0 17" fill="none" stroke="#0d1b3e" stroke-width="1.6"/></svg>
        <span>www.MarlowLaw.example</span>
      </div>
    </div>
  </footer>
</section>

<section class="card card-front">
  <div class="brand-mark"><span class="dot"></span>Marlow Law</div>
  <div class="card-name">MARLOW LAW GROUP, PLLC</div>
  <div class="card-rule"></div>
  <div class="card-tagline">INJURY ATTORNEYS</div>
</section>

<section class="card card-back">
  <div class="card-back-band"></div>
  <div class="brand-mark">Marlow<br>Law</div>
  <div class="card-name">MARLOW LAW GROUP, PLLC</div>
  <div class="card-rule"></div>
  <div class="card-tagline">INJURY ATTORNEYS</div>
  <div class="person">Tessa Quill</div>
  <div class="card-contacts">
    <div class="contact-item">
      <svg width="8" height="8" viewBox="0 0 24 24"><path fill="#0d1b3e" d="M6.6 10.8a15 15 0 0 0 6.6 6.6l2.2-2.2a1 1 0 0 1 1-.25 11 11 0 0 0 3.6.6 1 1 0 0 1 1 1V20a1 1 0 0 1-1 1A17 17 0 0 1 3 4a1 1 0 0 1 1-1h3.5a1 1 0 0 1 1 1c0 1.25.2 2.45.6 3.6a1 1 0 0 1-.25 1z"/></svg>
      <span>713-555-4718</span>
    </div>
    <div class="contact-item">
      <svg width="8" height="7" viewBox="0 0 24 18"><rect x="1" y="1" width="22" height="16" fill="#0d1b3e"/><path d="M1 1l11 9 11-9" fill="none" stroke="#fff" stroke-width="2"/></svg>
      <span>tessa@MarlowLaw.example</span>
    </div>
    <div class="contact-item">
      <svg width="7" height="9" viewBox="0 0 20 24"><path fill="#0d1b3e" d="M10 0a8 8 0 0 0-8 8c0 6 8 16 8 16s8-10 8-16a8 8 0 0 0-8-8zm0 11a3 3 0 1 1 0-6 3 3 0 0 1 0 6z"/></svg>
      <span>2150 Fernbrook Avenue, Suite 310,<br>Houston, Texas 77019</span>
    </div>
    <div class="contact-item">
      <svg width="8" height="8" viewBox="0 0 20 20"><circle cx="10" cy="10" r="8.5" fill="none" stroke="#0d1b3e" stroke-width="2"/><path d="M1.5 10h17M10 1.5c-4 4.5-4 12.5 0 17M10 1.5c4 4.5 4 12.5 0 17" fill="none" stroke="#0d1b3e" stroke-width="1.6"/></svg>
      <span>www.MarlowLaw.example</span>
    </div>
  </div>
</section>

</body>
</html>
```